Investment Firm Needs a Business Card Design

Need a business card for a new professional services firm that provides financial planning and investment management. Design should communicate financial safety and innovation. The contact information that needs to be on card is under Must Haves.

Target Market(s)

Retail Public

Industry/Entity Type

Investment

Requirements
Must have
• The data that needs to appear is in quotations:
"Darren Whitcombe, RWA"
(RWA logo either below my name or near my name)

"4417 Marlowe Lane
Suite 305
St. Charles, IL 60389"

"800-547-3162" (office)
"630-924-7318" (cell)
"darren@ledgerbeacon.net" (email)
"www.LedgerBeacon.net"
Nice to have
• would like to have the tag line "Steady Horizon(r)" with registered trade mark somewhere on card, maybe on back.

```html
<!DOCTYPE html>
<html lang="en">
<head>
<meta charset="utf-8">
<title>Ledger Beacon – Business Card</title>
<link rel="stylesheet" href="https://fonts.googleapis.com/css2?family=Cabin:wght@400;600;700&family=Alegreya+Sans:ital,wght@1,400&display=swap">
<style>
  :root {
    --navy: #1e2456;
    --ink: #141414;
    --tagline: #1f2a4f;
    --rule: #3a4470;
    --badge-blue: #1f5ea8;
    --paper: #ffffff;
  }
  * { margin: 0; padding: 0; box-sizing: border-box; }
  html, body {
    width: 1200px; height: 667px; overflow: hidden; background: var(--paper);
  }
  .card {
    position: relative; width: 1200px; height: 667px; background: var(--paper);
    font-family: "Cabin", sans-serif; color: var(--ink);
  }
  .brand {
    position: absolute; left: 175px; top: 62px;
    display: flex; align-items: center; gap: 48px;
  }
  .brand-square { width: 150px; height: 150px; background: var(--navy); }
  .brand-name {
    font-family: "Cabin", sans-serif; font-weight: 600; font-size: 66px;
    font-variant: small-caps; letter-spacing: 2px; color: var(--navy);
    line-height: 1;
  }
  .taglines {
    position: absolute; left: 78px; top: 358px; width: 360px;
    text-align: center; list-style: none;
    font-family: "Alegreya Sans", sans-serif; font-style: italic;
    font-size: 33px; color: var(--tagline);
  }
  .taglines li { line-height: 48px; }
  .taglines .divider {
    height: 1px; width: 119px; margin: 17px auto 20px; background: var(--rule);
  }
  .taglines sup { font-size: 16px; font-style: normal; vertical-align: 14px; line-height: 0; }
  .contact {
    position: absolute; left: 620px; top: 312px; width: 494px; text-align: center;
  }
  .person-name {
    font-weight: 700; font-size: 37px; letter-spacing: 0.5px; color: var(--ink);
    line-height: 48px;
  }
  .credential-row {
    display: flex; align-items: center; justify-content: space-between;
    margin-top: 12px; height: 80px;
  }
  .credential-row .rule { width: 114px; height: 1px; background: var(--rule); }
  .details { margin-top: 10px; font-size: 25px; line-height: 34px; color: var(--ink); }
  .footer-band {
    position: absolute; left: 0; bottom: 0; width: 1200px; height: 57px;
    background: var(--navy); color: var(--paper);
    display: flex; align-items: center; justify-content: center; gap: 34px;
    font-family: "Cabin", sans-serif; font-size: 20px; letter-spacing: 0.3px;
  }
</style>
</head>
<body>
  <div class="card">
    <div class="brand">
      <div class="brand-square"></div>
      <div class="brand-name">Ledger Beacon</div>
    </div>

    <ul class="taglines">
      <li>provide financial planning</li>
      <li class="divider" aria-hidden="true"></li>
      <li>investment management</li>
      <li class="divider" aria-hidden="true"></li>
      <li>steady horizon<sup>®</sup></li>
    </ul>

    <div class="contact">
      <div class="person-name">DARREN WHITCOMBE, RWA</div>
      <div class="credential-row">
        <span class="rule"></span>
        <svg class="credential-badge" width="84" height="80" viewBox="0 0 84 80" role="img" aria-label="Credential badge">
          <circle cx="42" cy="40" r="39" fill="var(--badge-blue)"/>
        </svg>
        <span class="rule"></span>
      </div>
      <div class="details">
        <div class="email">email: darren@ledgerbeacon.net</div>
        <div class="phone">office: 800-547-3162</div>
        <div class="phone">cell: 630-924-7318</div>
      </div>
    </div>

    <div class="footer-band">
      <span class="address">4417 Marlowe Lane, Suite 305, St. Charles, IL 60389</span>
      <span class="website">www.LedgerBeacon.net</span>
    </div>
  </div>
</body>
</html>
```